Olive Oil label for bottle 0.5l approx. 10x12 cm

I am running a Spa hotel in Bavaria (logo attached) and my family lives in Greece (Bavarian and Greek flag have the same colors). They produce organic olive oil first cold pressed extra virgin. I would need a label for 0,5 liter bottles to reach them out to my guests and they should see the high quality of the olive oil and the family connection Spa-hotel Bavaria to family in Greece. The name of the family is Morvatek, the hotel is called Tannegg, the olive oil comes from Greece/Argolis/Kranidi. The name of the small olive company is Kerano Hawks. There should be a space for the best before date and the organic control number (handwritten) . The hotel logo is not mandatory. Should look nice 😉

```html
<!DOCTYPE html>
<html lang="en">
<head>
<meta charset="utf-8">
<title>Kerano Hawks – Extra Virgin Olive Oil Label</title>
<link rel="stylesheet" href="https://fonts.googleapis.com/css2?family=Abril+Fatface&family=Playfair+Display:wght@700;900&display=swap">
<style>
  :root {
    --backdrop: #dadde3;
    --paper: #ffffff;
    --ink: #0e0e0e;
    --sage: #989c88;
    --slate-green: #53665f;
    --crackle: #1a1a18;
  }
  html, body {
    margin: 0;
    padding: 0;
    width: 971px;
    height: 1200px;
    overflow: hidden;
    background: var(--backdrop);
  }
  .label {
    position: absolute;
    left: 83px;
    top: 35px;
    width: 805px;
    height: 1130px;
    display: block;
  }
  .label-paper { fill: var(--paper); }
  .ink-fill { fill: var(--ink); }
  .sage-fill { fill: var(--sage); }
  .brand-ring { fill: none; stroke: var(--ink); stroke-width: 3; }
  .brand-disc { fill: var(--sage); }
  .brand-name {
    font-family: "Playfair Display", serif;
    font-weight: 700;
    font-size: 30px;
    letter-spacing: 0.22em;
    fill: var(--ink);
  }
  .tagline {
    font-family: "Playfair Display", serif;
    font-weight: 700;
    font-size: 21px;
    letter-spacing: 0.2em;
    fill: var(--ink);
  }
  .title-olive-caps {
    font-family: "Abril Fatface", serif;
    font-size: 290px;
    fill: var(--sage);
  }
  .title-olive-lower {
    font-family: "Abril Fatface", serif;
    font-size: 235px;
    fill: var(--sage);
  }
  .title-oil {
    font-family: "Abril Fatface", serif;
    font-size: 236px;
    fill: var(--slate-green);
  }
  .grade-text {
    font-family: "Playfair Display", serif;
    font-weight: 900;
    font-size: 32px;
    fill: var(--paper);
  }
  .rule { stroke: var(--ink); stroke-width: 3; }
  .field-box { fill: var(--paper); stroke: var(--ink); stroke-width: 3; }
  .field-label {
    font-family: "Playfair Display", serif;
    font-weight: 900;
    font-size: 19px;
    fill: var(--paper);
  }
  .field-dash { stroke: var(--paper); stroke-width: 2.5; stroke-dasharray: 12 7; }
  .crackle-band { fill: var(--crackle); }
  .volume {
    font-family: "Abril Fatface", serif;
    font-size: 56px;
    fill: var(--paper);
  }
</style>
</head>
<body>
<svg class="label" viewBox="0 0 805 1130" xmlns="http://www.w3.org/2000/svg">
  <rect class="label-paper" x="0" y="0" width="805" height="1130"/>

  <!-- top tab and brand -->
  <rect class="ink-fill" x="347" y="0" width="113" height="65"/>
  <circle class="brand-disc" cx="404" cy="135" r="70"/>
  <circle class="brand-ring" cx="404" cy="135" r="79"/>
  <text class="brand-name" x="404" y="256" text-anchor="middle">KERANO HAWKS</text>

  <!-- title: "Ol" on the low baseline, "ive" raised so "Oil" nests beneath -->
  <text class="tagline" x="478" y="397" textLength="227" lengthAdjust="spacingAndGlyphs">COLD PRESSED</text>
  <text class="title-olive-caps" x="99" y="577" textLength="299" lengthAdjust="spacingAndGlyphs">Ol</text>
  <text class="title-olive-lower" x="407" y="535" textLength="301" lengthAdjust="spacingAndGlyphs">ive</text>

  <line class="rule" x1="99" y1="593" x2="400" y2="593"/>
  <rect class="ink-fill" x="99" y="602" width="296" height="70"/>
  <line class="rule" x1="99" y1="683" x2="400" y2="683"/>
  <text class="grade-text" x="113" y="649" textLength="262" lengthAdjust="spacingAndGlyphs">EXTRA VIRGIN</text>

  <text class="title-oil" x="397" y="721" textLength="309" lengthAdjust="spacingAndGlyphs">Oil</text>

  <!-- handwritten fields -->
  <rect class="field-box" x="127" y="763" width="552" height="166"/>
  <rect class="ink-fill" x="126" y="762" width="237" height="168"/>
  <line class="rule" x1="363" y1="846" x2="679" y2="846"/>
  <text class="field-label" x="142" y="811" textLength="147" lengthAdjust="spacingAndGlyphs">BEST BEFORE</text>
  <line class="field-dash" x1="142" y1="843" x2="350" y2="843"/>
  <text class="field-label" x="142" y="897" textLength="211" lengthAdjust="spacingAndGlyphs">ORGANIC CONTROL</text>

  <!-- bottom band -->
  <rect class="sage-fill" x="0" y="1023" width="320" height="16"/>
  <rect class="sage-fill" x="486" y="1023" width="319" height="16"/>
  <rect class="crackle-band" x="0" y="1039" width="320" height="91" role="img" aria-label="Dark crackled stone texture band"/>
  <rect class="crackle-band" x="486" y="1039" width="319" height="91" role="img" aria-label="Dark crackled stone texture band"/>
  <polygon class="ink-fill" points="327,995 403,972 479,995 479,1130 327,1130"/>
  <text class="volume" x="403" y="1088" text-anchor="middle">0.5l</text>
</svg>
</body>
</html>
```